LuMarking-Tagvelory Partial Redesign - Web App

Are you able to apply your creativity to an existing layout? I’m convinced that even just a few touches can make a big difference to add personality and professionalism to a website design, and I’m looking for someone able to use existing ideas and bring them to the next level while keeping inside some given constraints.
The actual job is to improve an existing design concept and to apply it creatively to a landing page, a simple home page, and an older web app (single page website).
To help you start with a clear picture of the current situation and of my requirements, I created a detailed brief with screenshots, live examples, and complete instructions. You can find it attached to this job.
My tastes are inclined towards clean and simple designs. For this project I'm not looking for dazzling novelty, but for very solid craftsmanship. Are the right man - or woman - for the job?
Updates
I wanted to thank everybody who participated in this project. I made a choice, but also other designs were interesting. Hope to work with you another time.
Target Market(s)
Our main target is social media marketers and startuppers
Look and feel
Each slider illustrates characteristics of the customer's brand and the style your logo design should communicate.

```html
<!DOCTYPE html>
<html lang="en">
<head>
<meta charset="utf-8">
<title>LuMarking – Hashtag Summary</title>
<link rel="stylesheet" href="https://fonts.googleapis.com/css2?family=Arimo:ital,wght@0,400;0,700;1,400;1,700&family=Gelasio:wght@400&display=swap">
<style>
:root{
  --bar:#1f1f1f;
  --bar-top:#3a3a3a;
  --btn:#3d3d3d;
  --btn-edge:#555;
  --ink:#111;
  --muted:#666;
  --link:#2a8ac8;
  --panel:#f3f3f3;
  --panel-edge:#cfcfcf;
  --band:#a2acb1;
  --white:#fff;
  --green:#3a9b1a;
  --red:#e25b32;
  --pie-blue:#2d86c9;
  --pie-red:#d8401f;
  --gauge-red:#d9401d;
  --gauge-orange:#f39a1c;
  --gauge-green:#1e9a1e;
}
*{box-sizing:border-box;margin:0;padding:0}
html,body{width:847px;height:1200px;overflow:hidden;background:var(--white)}
body{position:relative;font-family:"Arimo",Arial,sans-serif;color:var(--ink)}
.abs{position:absolute}

.topbar{left:0;top:0;width:847px;height:43px;background:linear-gradient(var(--bar-top),var(--bar))}
.brand{position:absolute;color:var(--white);font-weight:700;font-size:14px;display:flex;align-items:center;gap:7px}
.brand::before{content:"";width:12px;height:12px;border-radius:50%;background:var(--white)}
.topbar .brand{left:34px;top:14px}
.navbtn{position:absolute;top:10px;height:25px;border-radius:3px;background:var(--btn);border:1px solid var(--btn-edge);color:var(--white);font-size:11px;display:flex;align-items:center;justify-content:center}
.navbtn.home{left:168px;width:40px;background:#111}
.navbtn.products{left:215px;width:71px}
.navbtn.blog{left:580px;width:40px}
.navbtn.about{left:628px;width:40px}
.navbtn.help{left:674px;width:41px}
.account{position:absolute;left:740px;top:14px;color:var(--white);font-size:11px;display:flex;align-items:center;gap:8px}
.caret{left:772px;top:43px;width:0;height:0;border-left:6px solid transparent;border-right:6px solid transparent;border-top:6px solid var(--bar)}

.page-title{left:38px;top:84px;font-size:23px;font-weight:400}
.page-title span{color:var(--link)}
.tracked{left:38px;top:115px;font-size:11px;font-style:italic;font-weight:700}
.tracked span{color:var(--link)}

.tab{position:absolute;top:138px;height:23px;background:linear-gradient(#f6f6f6,#dcdcdc);border:1px solid var(--panel-edge);border-bottom:none;border-radius:4px 4px 0 0;font-size:11px;display:flex;align-items:center;justify-content:center}
.tab.active{background:var(--panel);z-index:2;height:24px}
.tab.summary{left:534px;width:70px}
.tab.timeline{left:606px;width:66px}
.tab.influencers{left:673px;width:68px}
.tab.hashtags{left:742px;width:72px}

.panel{left:24px;top:160px;width:799px;height:922px;background:var(--panel);border:1px solid var(--panel-edge);border-radius:4px;box-shadow:0 1px 3px rgba(0,0,0,.15)}

.stat{position:absolute;top:212px;text-align:center}
.stat .num{font-family:"Gelasio",Georgia,serif;font-size:19px}
.stat .label{font-size:11px;font-style:italic;font-weight:700;margin-top:4px}
.stat.link .num,.stat.link .label{color:var(--link);font-weight:400}
.stat.link .label{font-weight:400}
.divider{position:absolute;top:206px;width:1px;height:64px;background:#d8d8d8}

.band{left:34px;width:780px;height:27px;background:var(--band);border-radius:3px;color:var(--white);font-size:17px;display:flex;align-items:center;justify-content:center}

.chart-title{position:absolute;font-size:13px;font-weight:700;text-align:center;width:380px}
.chart-title .with{color:var(--green)}
.chart-title .without{color:var(--red)}

.gauge{position:absolute;width:240px;height:240px}
.pie{position:absolute;width:160px;height:160px}
.legend{position:absolute;font-size:10px;line-height:12px}
.legend li{list-style:none;display:flex;gap:6px;margin-bottom:3px}
.legend li::before{content:"";flex:0 0 8px;height:8px;margin-top:2px;background:var(--c)}

.footer{left:0;top:1102px;width:847px;height:98px;background:var(--bar)}
.footer .brand{left:34px;top:18px}
.footer-rule{left:34px;top:46px;width:120px;height:1px;background:#444}
.address{left:34px;top:58px;color:var(--white);font-size:10px;font-weight:700;line-height:17px}
.copyright{left:345px;top:66px;color:var(--white);font-size:10px;font-weight:700}
.legal{top:66px;color:var(--white);font-size:10px;font-weight:700}
</style>
</head>
<body>

<header class="abs topbar">
  <div class="brand">LuMarking</div>
  <div class="navbtn home" aria-label="Home">
    <svg width="14" height="12" viewBox="0 0 14 12"><path d="M7 0 L14 6 H12 V12 H8.5 V8 H5.5 V12 H2 V6 H0 Z" fill="#fff"/></svg>
  </div>
  <div class="navbtn products">Products&nbsp;<svg width="8" height="5" viewBox="0 0 8 5"><path d="M0 0H8L4 5Z" fill="#fff"/></svg></div>
  <div class="navbtn blog">Blog</div>
  <div class="navbtn about">About</div>
  <div class="navbtn help">Help</div>
  <div class="account">
    <svg width="11" height="12" viewBox="0 0 11 12"><circle cx="5.5" cy="3.2" r="3.2" fill="#fff"/><path d="M0 12 C0 7 11 7 11 12Z" fill="#fff"/></svg>
    Account
  </div>
</header>
<div class="abs caret"></div>

<h1 class="abs page-title">Hashtag: <span>#socialtips</span></h1>
<p class="abs tracked">Tracked influencers: <span>@edwinmarlow</span>, <span>@redcoralmedia</span></p>

<div class="tab summary active">Summary</div>
<div class="tab timeline">Timeline</div>
<div class="tab influencers">Influencers</div>
<div class="tab hashtags">Hashtags</div>

<main class="abs panel"></main>

<div class="stat" style="left:54px;width:112px"><div class="num">8</div><div class="label">Observed Days</div></div>
<div class="divider" style="left:187px"></div>
<div class="stat link" style="left:205px;width:140px"><div class="num">8,492,949</div><div class="label">Total Impressions</div></div>
<div class="divider" style="left:360px"></div>
<div class="stat link" style="left:378px;width:100px"><div class="num">843</div><div class="label">Total Tweets</div></div>
<div class="divider" style="left:498px"></div>
<div class="stat" style="left:516px;width:140px"><div class="num">1,061,619</div><div class="label">Daily Impressions</div></div>
<div class="divider" style="left:674px"></div>
<div class="stat" style="left:692px;width:100px"><div class="num">105</div><div class="label">Daily Tweets</div></div>

<div class="abs band" style="top:318px">TREND ANALYSIS</div>

<div class="chart-title" style="left:31px;top:393px">Trend <span class="with">With</span> Your Influencers</div>
<div class="chart-title" style="left:441px;top:393px">Trend <span class="without">Without</span> Your Influencers</div>

<svg class="gauge" style="left:101px;top:440px" viewBox="-120 -120 240 240" aria-label="Trend gauge with influencers: 3">
  <defs>
    <linearGradient id="ring" x1="0" y1="0" x2="0" y2="1"><stop offset="0" stop-color="#f2f2f2"/><stop offset="1" stop-color="#b9b9b9"/></linearGradient>
    <radialGradient id="face" cx=".5" cy=".4" r=".6"><stop offset="0" stop-color="#fff"/><stop offset="1" stop-color="#e4e4e4"/></radialGradient>
  </defs>
  <circle r="116" fill="url(#ring)" stroke="#c4c4c4"/>
  <circle r="103" fill="url(#face)"/>
  <path d="M-70.7 70.7 A100 100 0 0 1 -64.3 -76.6 L-51.4 -61.3 A80 80 0 0 0 -56.6 56.6Z" fill="var(--gauge-red)"/>
  <path d="M-64.3 -76.6 A100 100 0 0 1 64.3 -76.6 L51.4 -61.3 A80 80 0 0 0 -51.4 -61.3Z" fill="var(--gauge-orange)"/>
  <path d="M64.3 -76.6 A100 100 0 0 1 70.7 70.7 L56.6 56.6 A80 80 0 0 0 51.4 -61.3Z" fill="var(--gauge-green)"/>
  <ellipse cx="0" cy="-52" rx="78" ry="44" fill="#fff" opacity=".22"/>
  <g stroke="#fff" stroke-width="2">
    <line y1="-98" y2="-86" transform="rotate(-108)"/><line y1="-98" y2="-86" transform="rotate(-81)"/><line y1="-98" y2="-86" transform="rotate(-54)"/>
    <line y1="-98" y2="-86" transform="rotate(-27)"/><line y1="-98" y2="-86" transform="rotate(27)"/><line y1="-98" y2="-86" transform="rotate(54)"/>
    <line y1="-98" y2="-86" transform="rotate(81)"/><line y1="-98" y2="-86" transform="rotate(108)"/>
  </g>
  <text y="-62" text-anchor="middle" font-size="10" fill="var(--gauge-orange)">0</text>
  <text x="-48" y="52" text-anchor="middle" font-size="10" fill="var(--gauge-red)">-100</text>
  <text x="50" y="52" text-anchor="middle" font-size="10" fill="var(--gauge-green)">100</text>
  <text y="35" text-anchor="middle" font-size="18" fill="#777">Trend</text>
  <text y="80" text-anchor="middle" font-size="24" fill="#777">3</text>
  <polygon points="-3,14 3,14 1,-80 -1,-80" fill="#6f6f6f" transform="rotate(-63)"/>
  <circle r="13" fill="#c9c9c9"/><circle r="8" fill="#aaa"/>
</svg>

<svg class="gauge" style="left:509px;top:440px" viewBox="-120 -120 240 240" aria-label="Trend gauge without influencers: 3">
  <circle r="116" fill="url(#ring)" stroke="#c4c4c4"/>
  <circle r="103" fill="url(#face)"/>
  <path d="M-70.7 70.7 A100 100 0 0 1 -64.3 -76.6 L-51.4 -61.3 A80 80 0 0 0 -56.6 56.6Z" fill="var(--gauge-red)"/>
  <path d="M-64.3 -76.6 A100 100 0 0 1 64.3 -76.6 L51.4 -61.3 A80 80 0 0 0 -51.4 -61.3Z" fill="var(--gauge-orange)"/>
  <path d="M64.3 -76.6 A100 100 0 0 1 70.7 70.7 L56.6 56.6 A80 80 0 0 0 51.4 -61.3Z" fill="var(--gauge-green)"/>
  <ellipse cx="0" cy="-52" rx="78" ry="44" fill="#fff" opacity=".22"/>
  <g stroke="#fff" stroke-width="2">
    <line y1="-98" y2="-86" transform="rotate(-108)"/><line y1="-98" y2="-86" transform="rotate(-81)"/><line y1="-98" y2="-86" transform="rotate(-54)"/>
    <line y1="-98" y2="-86" transform="rotate(-27)"/><line y1="-98" y2="-86" transform="rotate(27)"/><line y1="-98" y2="-86" transform="rotate(54)"/>
    <line y1="-98" y2="-86" transform="rotate(81)"/><line y1="-98" y2="-86" transform="rotate(108)"/>
  </g>
  <text y="-62" text-anchor="middle" font-size="10" fill="var(--gauge-orange)">0</text>
  <text x="-48" y="52" text-anchor="middle" font-size="10" fill="var(--gauge-red)">-100</text>
  <text x="50" y="52" text-anchor="middle" font-size="10" fill="var(--gauge-green)">100</text>
  <text y="35" text-anchor="middle" font-size="18" fill="#777">Trend</text>
  <text y="80" text-anchor="middle" font-size="24" fill="#777">3</text>
  <polygon points="-3,14 3,14 1,-80 -1,-80" fill="#6f6f6f" transform="rotate(18)"/>
  <circle r="13" fill="#c9c9c9"/><circle r="8" fill="#aaa"/>
</svg>

<div class="abs band" style="top:743px">TOUR INFLUENCERS ANALYSIS</div>

<div class="chart-title" style="left:31px;top:820px">Your Influencers vs Rest Of The Internet</div>
<div class="chart-title" style="left:441px;top:820px">Your Influencers vs Your influencers</div>

<svg class="pie" style="left:130px;top:884px" viewBox="-80 -80 160 160" aria-label="Tracked influencers 75%, others 25%">
  <path d="M0 0 L77 0 A77 77 0 1 1 0 -77Z" fill="var(--pie-blue)" stroke="#fff"/>
  <path d="M0 0 L0 -77 A77 77 0 0 1 77 0Z" fill="var(--pie-red)" stroke="#fff"/>
  <text x="35" y="-26" text-anchor="middle" font-size="10" fill="#fff">25%</text>
  <text x="-40" y="32" text-anchor="middle" font-size="10" fill="#fff">75%</text>
</svg>
<ul class="legend" style="left:304px;top:868px;width:70px">
  <li style="--c:var(--pie-blue)">Tracked Influencers</li>
  <li style="--c:var(--pie-red)">Others</li>
</ul>

<svg class="pie" style="left:520px;top:884px" viewBox="-80 -80 160 160" aria-label="redcoralmedia 75%, edwinmarlow 25%">
  <path d="M0 0 L77 0 A77 77 0 1 1 0 -77Z" fill="var(--pie-blue)" stroke="#fff"/>
  <path d="M0 0 L0 -77 A77 77 0 0 1 77 0Z" fill="var(--pie-red)" stroke="#fff"/>
  <text x="35" y="-26" text-anchor="middle" font-size="10" fill="#fff">25%</text>
  <text x="-40" y="32" text-anchor="middle" font-size="10" fill="#fff">75%</text>
</svg>
<ul class="legend" style="left:694px;top:868px;width:90px">
  <li style="--c:var(--pie-blue)">redcoralm...</li>
  <li style="--c:var(--pie-red)">edwinmarlow</li>
</ul>

<footer class="abs footer">
  <div class="brand">LuMarking</div>
  <div class="abs footer-rule"></div>
  <address class="abs address" style="font-style:normal">48 Larch Street<br>E9 4QT London, UK</address>
  <p class="abs copyright">Copyright © 2012 LuMarking Ltd.</p>
  <p class="abs legal" style="left:655px">Private Policy</p>
  <p class="abs legal" style="left:732px">Term Of Services</p>
</footer>

</body>
</html>
```